Infographic for Anesthesia Management Company

I would like my Anesthesia Management company, Veltrin Anesthesia, service information placed into a infographic for use on a brochure and webpage. Please focus on just the infographic.
-Veltrin Services text to be placed into infographic attached in word file.
-Two Vector infographic templates attached as well. I am open to either option, or alternative layout suggestion.
-Please match color scheme to veltrinanesthesia-example.com
-Veltrin logo attached.
Thank you for your help!
Marvin
Target Market(s)
Surgery Centers
Industry/Entity Type
It Company
Font styles to use
Requirements
Must have
- Professional Look.
- Easy to read text.
- Cohesive branding
Nice to have
- Please see attached Vector examples.

```html
<!DOCTYPE html>
<html lang="en">
<head>
<meta charset="utf-8">
<title>Veltrin Anesthesia – Provider Recruitment, Credentialing, and Staffing</title>
<link href="https://fonts.googleapis.com/css2?family=Exo+2:wght@400;500;600&family=Montserrat:wght@700&family=Figtree:wght@400&display=swap" rel="stylesheet">
<style>
  :root{
    --charcoal:#404040;
    --teal:#1db59b;
    --purple:#7b6d96;
    --ink:#333333;
    --panel:#ffffff;
    --page:#ececec;
    --rule:#6b6b6b;
  }
  *{margin:0;padding:0;box-sizing:border-box}
  html,body{width:1200px;height:728px;overflow:hidden;background:#fff}
  .canvas{position:relative;width:1200px;height:728px;background:var(--page);font-family:"Figtree",sans-serif;color:var(--ink)}
  .header-band{position:absolute;left:0;top:0;width:1200px;height:122px;background:var(--charcoal)}
  .header-tab{position:absolute;left:160px;top:60px;width:854px;height:82px;background:var(--charcoal);border-radius:0 0 24px 24px}
  .title{position:absolute;left:0;top:28px;width:1154px;text-align:center;color:#fff;font-family:"Montserrat",sans-serif;font-weight:700;font-size:40px;line-height:48px;letter-spacing:.5px}
  .panel{position:absolute;background:var(--panel);box-shadow:0 1px 4px rgba(0,0,0,.12)}
  .panel-pro{left:30px;top:157px;width:393px;height:297px}
  .panel-acc{left:434px;top:157px;width:392px;height:297px}
  .panel-eff{left:836px;top:157px;width:330px;height:297px}
  .panel-safety{left:30px;top:462px;width:1136px;height:246px;border-radius:0 0 24px 24px}
  .chevron{position:absolute;top:285px;width:26px;height:40px}
  .icon{position:absolute;background:var(--teal);border-radius:10px}
  .heading{position:absolute;font-family:"Exo 2",sans-serif;font-weight:600;font-size:28px;color:var(--charcoal);letter-spacing:.5px;line-height:34px}
  .subhead{position:absolute;font-family:"Exo 2",sans-serif;font-weight:500;font-size:20px;color:var(--purple);line-height:24px}
  .rule{position:absolute;border-top:1px dashed var(--rule)}
  .item{position:absolute;font-size:12.6px;line-height:16.4px;color:var(--ink)}
  .tick{position:absolute;width:19px;height:19px}
  .divider{position:absolute;left:813px;top:492px;width:1px;height:196px;background:var(--purple)}
  .brand{position:absolute;left:880px;top:500px;width:270px;text-align:center;font-family:"Exo 2",sans-serif;font-weight:600;font-size:34px;color:var(--teal);line-height:40px}
  .phone{position:absolute;left:830px;top:578px;width:346px;text-align:center;font-family:"Exo 2",sans-serif;font-weight:500;font-size:46px;color:var(--purple);line-height:54px}
  .web{position:absolute;left:830px;top:632px;width:346px;text-align:center;font-family:"Exo 2",sans-serif;font-weight:500;font-size:20px;color:var(--charcoal)}
  .email{position:absolute;left:830px;top:659px;width:346px;text-align:center;font-family:"Exo 2",sans-serif;font-weight:500;font-size:15px;color:var(--charcoal)}
</style>
</head>
<body>
<svg width="0" height="0" style="position:absolute">
  <defs>
    <symbol id="tick" viewBox="0 0 20 20">
      <circle cx="10" cy="10" r="8.3" fill="none" stroke="#1db59b" stroke-width="2"/>
      <path d="M6 10.2l2.7 2.7L14.2 7.4" fill="none" stroke="#1db59b" stroke-width="2.2" stroke-linecap="round" stroke-linejoin="round"/>
    </symbol>
    <symbol id="chev" viewBox="0 0 26 40">
      <path d="M0 0h10l16 20-16 20H0l16-20z" fill="#e4e4e4"/>
    </symbol>
  </defs>
</svg>

<div class="canvas">
  <div class="header-band"></div>
  <div class="header-tab"></div>
  <h1 class="title">ANESTHESIA PROVIDER RECRUITMENT,<br>CREDENTIALING, AND STAFFING</h1>

  <!-- Professionalism -->
  <section class="panel panel-pro">
    <div class="icon" style="left:14px;top:28px;width:88px;height:56px;border-radius:28px" role="img" aria-label="Handshake icon"></div>
    <h2 class="heading" style="left:109px;top:22px">PROFESSIONALISM</h2>
    <p class="subhead" style="left:109px;top:66px">ASC Stakeholder Satisfaction</p>
    <div class="rule" style="left:63px;top:100px;width:307px"></div>
    <svg class="tick" style="left:73px;top:118px"><use href="#tick"/></svg>
    <p class="item" style="left:104px;top:114px">Share our personal network of highly<br>qualified anesthesia providers</p>
    <svg class="tick" style="left:73px;top:163px"><use href="#tick"/></svg>
    <p class="item" style="left:104px;top:160px">Create continuity between anesthesia,<br>surgeon, and ASC staff</p>
    <svg class="tick" style="left:73px;top:209px"><use href="#tick"/></svg>
    <p class="item" style="left:104px;top:206px">Guarantee every anesthesia provider<br>upholds clinical excellence</p>
    <svg class="tick" style="left:73px;top:254px"><use href="#tick"/></svg>
    <p class="item" style="left:104px;top:250px">Coordinate staffing to meet your<br>scheduled case volume</p>
  </section>

  <svg class="chevron" style="left:423px"><use href="#chev"/></svg>

  <!-- Accountability -->
  <section class="panel panel-acc">
    <div class="icon" style="left:28px;top:16px;width:64px;height:86px;border-radius:8px" role="img" aria-label="Clipboard checklist icon"></div>
    <h2 class="heading" style="left:118px;top:24px">ACCOUNTABILITY</h2>
    <p class="subhead" style="left:118px;top:66px">Meeting Accreditation<br>Requirements</p>
    <div class="rule" style="left:54px;top:127px;width:283px"></div>
    <svg class="tick" style="left:53px;top:141px"><use href="#tick"/></svg>
    <p class="item" style="left:84px;top:137px">Partner with your surgery center to ensure<br>anesthesia policies and procedures are up<br>to current ASC credentialing standards</p>
    <p class="subhead" style="left:88px;top:197px">In-House Billing</p>
    <div class="rule" style="left:46px;top:229px;width:284px"></div>
    <svg class="tick" style="left:53px;top:246px"><use href="#tick"/></svg>
    <p class="item" style="left:84px;top:235px">Dedicated in-house billers ensure<br>anesthesia billing is processed correctly<br>the first time</p>
  </section>

  <svg class="chevron" style="left:826px"><use href="#chev"/></svg>

  <!-- Efficiency -->
  <section class="panel panel-eff">
    <div class="icon" style="left:14px;top:16px;width:84px;height:84px;border-radius:50%" role="img" aria-label="Target with arrow icon"></div>
    <h2 class="heading" style="left:105px;top:44px">EFFICIENCY</h2>
    <p class="subhead" style="left:100px;top:81px">Thought Leadership</p>
    <div class="rule" style="left:53px;top:117px;width:226px"></div>
    <svg class="tick" style="left:74px;top:140px"><use href="#tick"/></svg>
    <p class="item" style="left:105px;top:137px">Stipend free anesthesia<br>services</p>
    <svg class="tick" style="left:74px;top:187px"><use href="#tick"/></svg>
    <p class="item" style="left:105px;top:184px">Proprietary and data-driven<br>process to maintain on-time<br>surgery flow</p>
  </section>

  <!-- Patient Safety -->
  <section class="panel panel-safety">
    <div class="icon" style="left:22px;top:30px;width:92px;height:86px;border-radius:40px 40px 20px 20px" role="img" aria-label="Heart with pulse line held in two hands icon"></div>
    <h2 class="heading" style="left:138px;top:36px;font-size:29px">PATIENT<br>SAFETY</h2>
    <p class="subhead" style="left:138px;top:110px">Clinical Guidance and<br>Quality Improvement</p>
    <svg class="tick" style="left:362px;top:45px"><use href="#tick"/></svg>
    <p class="item" style="left:398px;top:43px">Pre-operative protocols to minimize cancellations<br>and optimize patient outcomes</p>
    <svg class="tick" style="left:362px;top:92px"><use href="#tick"/></svg>
    <p class="item" style="left:398px;top:90px">Patient selection criteria to ensure suitable<br>surgical candidates</p>
    <svg class="tick" style="left:362px;top:138px"><use href="#tick"/></svg>
    <p class="item" style="left:398px;top:136px">Education programs to engage the clinical<br>staff</p>
    <svg class="tick" style="left:362px;top:180px"><use href="#tick"/></svg>
    <p class="item" style="left:398px;top:178px">Evidence based multimodal pain management protocol to<br>facilitate a timely discharge and reduce patient side effects</p>
  </section>

  <div class="divider"></div>
  <p class="brand">Veltrin Anesthesia</p>
  <p class="phone">(555) 014-2273</p>
  <p class="web">www.veltrinanesthesia-example.com</p>
  <p class="email">marvinb@veltrinanesthesia-example.com</p>
</div>
</body>
</html>
```